Santa Crying/Smiling Graphic for stickers and t-shirts

This graphic will be printed on t-shirts and stickers. It needs to be round in general shape. We will be giving stickers to kids after they take a photo with Santa Claus, Some kids cry, some smile.

The project needs to contain two graphic files, one of the smiling sticker, and one of the crying sticker. We are okay with a cartoon drawing if you want, or a text only design, but they need to go together but easily contrast each other. The text will say "I smiled for Santa" or "I cried for Santa". The design must have our logo as part of it somehow, and include the year "2016", as we want to renew this every year.

I included the logo we would like you to use. The smile graphic will be printed on mint blue, and the crying graphic will be printed on red. Please use colors that match that scheme. Thank you!
Updates

Target Market(s)

Families and children

Font styles to use
Sans Serif

Colors
ec1f27
cee9f5
0355a3
9bcb3c

Requirements
Must have
• "I smiled for Santa" in one design, printed on mint blue
• "I cried for Santa" in second design, printed on Christmas red
• "2016" on both
• Our logo on both
Nice to have
• Similar style for tboth
Should not have
• NA

```html
<!DOCTYPE html>
<html lang="en">
<head>
<meta charset="utf-8">
<title>I Smiled / I Cried for Santa – Sticker Set 2016</title>
<link rel="stylesheet" href="https://fonts.googleapis.com/css2?family=Signika:wght@300;400;600&family=Montserrat:wght@600&display=swap">
<style>
  :root {
    --mint: #45c3cf;
    --mint-deep: #2fa9b5;
    --christmas-red: #ec2329;
    --leaf-green: #9bcb3c;
    --leaf-deep: #7fb12a;
    --ink: #111111;
    --white: #ffffff;
    --blush: #f4a3a6;
    --silver: #b9b9bd;
    --page: #ffffff;
  }
  html, body {
    margin: 0;
    padding: 0;
    width: 1200px;
    height: 1000px;
    overflow: hidden;
    background: var(--page);
  }
  .sticker-sheet { display: block; width: 1200px; height: 1000px; }
  .sticker-disc--smile { fill: var(--mint); }
  .sticker-disc--cry { fill: var(--christmas-red); }
  .sticker-rim { fill: none; stroke: var(--white); stroke-width: 3; }
  .headline {
    font-family: "Signika", "Trebuchet MS", sans-serif;
    font-weight: 400;
    paint-order: stroke;
    stroke: var(--white);
    stroke-width: 3;
    stroke-linejoin: round;
  }
  .headline--verb { fill: var(--leaf-green); font-size: 88px; }
  .headline--verb-cry { font-size: 100px; }
  .headline--for { fill: var(--ink); font-weight: 600; font-size: 44px; stroke: none; }
  .headline--santa { font-size: 88px; }
  .headline--santa-red { fill: var(--christmas-red); }
  .headline--santa-mint { fill: var(--mint); }
  .mood-badge { stroke: var(--white); stroke-width: 4; }
  .mood-badge--smile { fill: url(#badgeGreen); }
  .mood-badge--cry { fill: url(#badgeMint); }
  .tree-art { fill: rgba(255,255,255,0.35); }
  .studio-name {
    font-family: "Montserrat", "Arial", sans-serif;
    font-weight: 600;
    fill: var(--blush);
    text-anchor: middle;
    paint-order: stroke;
    stroke: var(--white);
    stroke-width: 1.5;
  }
  .studio-name--main { font-size: 39px; letter-spacing: 2px; }
  .studio-name--sub { font-size: 24px; letter-spacing: 2px; fill: var(--silver); }
  .edition-year {
    font-family: "Montserrat", "Arial", sans-serif;
    font-weight: 600;
    font-size: 31px;
    letter-spacing: 2px;
    fill: var(--silver);
    text-anchor: middle;
    paint-order: stroke;
    stroke: var(--white);
    stroke-width: 1.5;
  }
</style>
</head>
<body>
<svg class="sticker-sheet" viewBox="0 0 1200 1000" xmlns="http://www.w3.org/2000/svg">
  <defs>
    <radialGradient id="badgeGreen" cx="40%" cy="35%" r="70%">
      <stop offset="0" stop-color="#b2da5c"/>
      <stop offset="1" stop-color="#7fb12a"/>
    </radialGradient>
    <radialGradient id="badgeMint" cx="40%" cy="35%" r="70%">
      <stop offset="0" stop-color="#62d0da"/>
      <stop offset="1" stop-color="#2fa9b5"/>
    </radialGradient>
  </defs>

  <g class="sticker sticker--smile">
    <circle class="sticker-disc--smile" cx="318" cy="407" r="283"/>
    <circle class="sticker-rim" cx="318" cy="407" r="268"/>
    <polygon class="tree-art" role="img" aria-label="Christmas tree made of white snowflakes, stars and candy canes with a Santa hat on the studio emblem" points="312,236 490,552 148,552"/>
    <circle class="mood-badge mood-badge--smile" role="img" aria-label="Round green smiling-face badge" cx="136" cy="362" r="64"/>
    <text class="headline headline--verb" transform="translate(124 276) rotate(-12)">I Smiled</text>
    <text class="headline headline--for" x="368" y="275">for</text>
    <text class="headline headline--santa headline--santa-red" x="322" y="335">Santa</text>
    <text class="studio-name studio-name--main" x="318" y="582">THE PINECROFTS’</text>
    <text class="studio-name studio-name--sub" x="318" y="612">PHOTOGRAPHY</text>
    <text class="edition-year" x="318" y="643">2016</text>
  </g>

  <g class="sticker sticker--cry">
    <circle class="sticker-disc--cry" cx="892" cy="407" r="283"/>
    <circle class="sticker-rim" cx="892" cy="407" r="268"/>
    <polygon class="tree-art" role="img" aria-label="Christmas tree made of white snowflakes, stars and candy canes with a Santa hat on the studio emblem" points="886,236 1064,552 722,552"/>
    <circle class="mood-badge mood-badge--cry" role="img" aria-label="Round mint crying-face badge" cx="706" cy="362" r="64"/>
    <text class="headline headline--verb headline--verb-cry" transform="translate(706 282) rotate(-12)">I Cried</text>
    <text class="headline headline--for" x="946" y="275">for</text>
    <text class="headline headline--santa headline--santa-mint" x="896" y="335">Santa</text>
    <text class="studio-name studio-name--main" x="892" y="582">THE PINECROFTS’</text>
    <text class="studio-name studio-name--sub" x="892" y="612">PHOTOGRAPHY</text>
    <text class="edition-year" x="892" y="643">2016</text>
  </g>
</svg>
</body>
</html>
```